Sales banner for E-commerce

This banner is intended for an e-commerce site selling motorcycle equipment and accessories.
The banner announces the sales and leads the customer to an offer of helmets, equipment, and accessories for motorcyclists.
The style of the banner must be modern, elegant, and both show that the prices are attractive and make you want to click to discover the offer of sale products behind it.
I insist on the aesthetics and the marketing side of the banner which are two absolutely essential elements.
Banner format 3840 (W) x 1250 (H)
Updates
Faible participation designers
Target Market(s)
Biker clientele in the general sense
Industry/Entity Type
Ecommerce Equipement et accessoires moto
Requirements
Must have
- Represent or inspire the motorcycle universe.
Nice to have
- The banner must be attractive and make you want to click

```html
<!DOCTYPE html>
<html lang="en">
<head>
<meta charset="UTF-8">
<title>Sales Banner for E-commerce</title>
<link rel="stylesheet" href="https://fonts.googleapis.com/css2?family=Poppins:wght@400&family=Montserrat:ital,wght@0,300;1,200;1,300;1,800&family=Roboto:wght@300;700&display=swap">
<style>
  :root {
    --board: #000000;
    --ink: #2a2a2a;
    --white: #ffffff;
    --pink: #e0215f;
    --yellow: #ffc600;
    --forest: #0c3a1d;
    --accent-red: #d8233f;
    --sky-top: #e6e9ec;
    --sky-mid: #f4f0ea;
    --dusk: #f1cfa6;
    --sun: #ffd9a0;
    --silhouette: #1c1b1e;
    --plaid: #1f8f4e;
    --plaid-dark: #166a3a;
    --road: #9a8368;
    --leaf: #3c5a2c;
    --leaf-dark: #141c10;
  }
  * { margin: 0; padding: 0; box-sizing: border-box; }
  html, body { width: 1200px; height: 1052px; overflow: hidden; background: var(--board); }
  .board { position: relative; width: 1200px; height: 1052px; background: var(--board); }
  .board-title {
    position: absolute; top: 96px; left: 0; width: 1200px; text-align: center;
    font-family: "Poppins", sans-serif; font-weight: 400; font-size: 38px;
    letter-spacing: 6px; color: var(--white);
  }
  .banner { position: absolute; left: 60px; width: 1080px; height: 351px; overflow: hidden; }
  .banner--sunset { top: 187px; }
  .banner--forest { top: 583px; }
  .banner-scene { position: absolute; inset: 0; }

  .banner--sunset .banner-scene {
    background:
      radial-gradient(ellipse 260px 120px at 300px 330px, rgba(255,190,110,0.85) 0%, rgba(255,200,140,0) 100%),
      radial-gradient(ellipse 520px 110px at 560px 360px, rgba(241,200,150,0.9) 0%, rgba(241,200,150,0) 100%),
      linear-gradient(180deg, var(--sky-top) 0%, var(--sky-mid) 62%, var(--dusk) 100%);
  }
  .banner--sunset .rider-photo {
    position: absolute; left: 0; top: 0; width: 440px; height: 351px;
    background:
      radial-gradient(ellipse 90px 110px at 360px 300px, rgba(255,196,120,0.55) 0%, rgba(255,196,120,0) 100%),
      linear-gradient(90deg, var(--silhouette) 0%, #242226 45%, rgba(40,38,40,0.75) 72%, rgba(40,38,40,0) 100%);
    -webkit-mask-image: linear-gradient(180deg, rgba(0,0,0,0.35) 0%, #000 28%, #000 100%);
            mask-image: linear-gradient(180deg, rgba(0,0,0,0.35) 0%, #000 28%, #000 100%);
  }

  .banner--forest .banner-scene {
    background:
      radial-gradient(ellipse 260px 200px at 470px 330px, rgba(160,138,108,0.95) 0%, rgba(160,138,108,0) 100%),
      radial-gradient(ellipse 300px 150px at 520px 60px, rgba(120,150,90,0.6) 0%, rgba(120,150,90,0) 100%),
      linear-gradient(90deg, var(--leaf) 0%, #2f4a24 55%, var(--leaf-dark) 100%);
  }
  .banner--forest .rider-photo {
    position: absolute; left: 0; top: 0; width: 470px; height: 351px;
    background:
      radial-gradient(ellipse 150px 170px at 250px 200px, rgba(222,222,212,0.9) 0%, rgba(222,222,212,0) 100%),
      radial-gradient(ellipse 80px 90px at 400px 270px, rgba(212,170,60,0.85) 0%, rgba(212,170,60,0) 100%),
      linear-gradient(90deg, var(--plaid-dark) 0%, var(--plaid) 40%, rgba(31,143,78,0.8) 75%, rgba(31,143,78,0) 100%);
  }

  .headline-lead, .headline-main, .headline-sub { position: absolute; white-space: nowrap; }
  .headline-lead {
    font-family: "Montserrat", sans-serif; font-style: italic; font-weight: 200; letter-spacing: 1px;
  }
  .headline-main {
    font-family: "Montserrat", sans-serif; font-style: italic; font-weight: 800;
    line-height: 1; letter-spacing: -4px;
  }
  .banner--sunset .headline-lead { left: 431px; top: 80px; font-size: 41px; color: var(--ink); }
  .banner--sunset .headline-main { left: 417px; top: 116px; font-size: 90px; color: var(--ink); }
  .banner--sunset .headline-sub {
    left: 417px; top: 202px; font-family: "Montserrat", sans-serif; font-style: italic;
    font-weight: 300; font-size: 14px; letter-spacing: 1.5px; color: var(--ink);
  }
  .banner--sunset .sub-rule {
    position: absolute; left: 417px; top: 225px; width: 314px; border-top: 1px dashed var(--pink);
  }
  .banner--forest .headline-lead { left: 468px; top: 78px; font-size: 47px; color: var(--white); }
  .banner--forest .headline-main { left: 457px; top: 121px; font-size: 86px; letter-spacing: -5px; color: var(--yellow); }
  .banner--forest .headline-sub {
    left: 459px; top: 192px; font-family: "Roboto", sans-serif; font-weight: 300;
    font-size: 17px; color: var(--white);
  }

  .cta {
    position: absolute; display: flex; align-items: center; justify-content: center;
    color: var(--white); font-family: "Montserrat", sans-serif;
    font-weight: 300; font-size: 7.5px; letter-spacing: 3px; text-decoration: none;
  }
  .cta::before {
    content: ""; position: absolute; left: 9px; top: 6px; width: 10px; height: 10px;
    border-top: 1px solid var(--white); border-left: 1px solid var(--white);
    border-top-left-radius: 10px;
  }
  .banner--sunset .cta { left: 413px; top: 247px; width: 142px; height: 35px; border-radius: 18px; background: var(--pink); padding-left: 4px; }
  .banner--forest .cta { left: 457px; top: 251px; width: 110px; height: 27px; border-radius: 14px; background: var(--forest); font-size: 6.5px; padding-left: 6px; }

  .product-image { position: absolute; border-radius: 50%; overflow: hidden; }
  .product-image--intercom { background: radial-gradient(ellipse 60% 34% at 50% 52%, #2a1a20 0%, #5a2a38 40%, #e8e8e8 78%, #f5f5f5 100%); }
  .product-image--helmet { background: radial-gradient(ellipse 44% 42% at 46% 52%, #19191b 0%, #2a2a2d 62%, #e2e2e2 82%, #ececec 100%); }
  .product-image--jacket { background: radial-gradient(ellipse 40% 46% at 50% 52%, #1d1f1d 0%, #2f3a2a 60%, #f3f3f3 84%, #ffffff 100%); }
  .product-image--glove { background: radial-gradient(ellipse 30% 44% at 50% 50%, #8c5a62 0%, #8d8f96 55%, #f0f0f0 84%, #f6f6f6 100%); }
  .banner--forest .product-image { box-shadow: 0 0 0 3px rgba(255,255,255,0.9); }

  .product-accent { position: absolute; }
  .price-was, .price-now { position: absolute; font-family: "Roboto", sans-serif; white-space: nowrap; }
  .price-was { font-size: 7px; text-decoration: line-through; }
  .price-now { font-size: 12px; font-weight: 700; }
  .banner--sunset .price-was, .banner--sunset .price-now { color: #111; }
  .banner--forest .price-was, .banner--forest .price-now { color: var(--white); }
</style>
</head>
<body>
<main class="board">
  <h1 class="board-title">SALES BANNER FOR E-COMMERCE</h1>

  <section class="banner banner--sunset">
    <div class="banner-scene" role="img" aria-label="Sunset sky over a city skyline with warm light near the road"></div>
    <div class="rider-photo" role="img" aria-label="Helmeted rider in black leather on a café racer motorcycle, backlit by the setting sun"></div>
    <p class="headline-lead">MADE FOR</p>
    <p class="headline-main">RIDERS</p>
    <p class="headline-sub">Helmets, Equipment, and Accessories</p>
    <div class="sub-rule"></div>
    <a class="cta" href="#">EXPLORE MORE</a>

    <div class="product-image product-image--intercom" style="left:824px;top:33px;width:68px;height:68px;" role="img" aria-label="Helmet Bluetooth intercom unit"></div>
    <span class="price-was" style="left:895px;top:38px;">$169.00</span>
    <span class="price-now" style="left:894px;top:45px;">$143.65</span>

    <svg class="product-accent" style="left:874px;top:96px;" width="96" height="90" viewBox="0 0 96 90"><path d="M44 0 A44 45 0 0 1 44 90 A48 45 0 0 0 44 0Z" fill="var(--accent-red)"/></svg>
    <div class="product-image product-image--helmet" style="left:874px;top:96px;width:88px;height:88px;" role="img" aria-label="Black full-face motorcycle helmet"></div>
    <span class="price-was" style="left:965px;top:103px;">$699.99</span>
    <span class="price-now" style="left:964px;top:110px;">$599.20</span>

    <div class="product-image product-image--jacket" style="left:804px;top:176px;width:68px;height:68px;" role="img" aria-label="Black touring motorcycle jacket with green accents"></div>
    <span class="price-now" style="left:879px;top:210px;">$299.99</span>

    <div class="product-image product-image--glove" style="left:853px;top:253px;width:68px;height:68px;" role="img" aria-label="Grey and red motorcycle glove"></div>
    <span class="price-was" style="left:927px;top:277px;">$49.95</span>
    <span class="price-now" style="left:926px;top:284px;">$47.75</span>
  </section>

  <section class="banner banner--forest">
    <div class="banner-scene" role="img" aria-label="Sunlit dirt road through a leafy green forest"></div>
    <div class="rider-photo" role="img" aria-label="Rider in a green flannel shirt holding a white vintage motocross helmet with goggles and yellow leather gloves"></div>
    <p class="headline-lead">MADE FOR</p>
    <p class="headline-main">RIDERS</p>
    <p class="headline-sub">Helmets, Equipment, and Accessories</p>
    <a class="cta" href="#">EXPLORE MORE</a>

    <div class="product-image product-image--intercom" style="left:824px;top:33px;width:68px;height:68px;" role="img" aria-label="Helmet Bluetooth intercom unit"></div>
    <span class="price-was" style="left:895px;top:38px;">$169.00</span>
    <span class="price-now" style="left:894px;top:45px;">$143.65</span>

    <svg class="product-accent" style="left:874px;top:96px;" width="96" height="90" viewBox="0 0 96 90"><path d="M44 0 A44 45 0 0 1 44 90 A48 45 0 0 0 44 0Z" fill="var(--accent-red)"/></svg>
    <div class="product-image product-image--helmet" style="left:874px;top:96px;width:88px;height:88px;" role="img" aria-label="Black full-face motorcycle helmet"></div>
    <span class="price-was" style="left:965px;top:103px;">$699.99</span>
    <span class="price-now" style="left:964px;top:110px;">$599.20</span>

    <div class="product-image product-image--jacket" style="left:804px;top:176px;width:68px;height:68px;" role="img" aria-label="Black touring motorcycle jacket with green accents"></div>
    <span class="price-now" style="left:879px;top:210px;">$299.99</span>

    <div class="product-image product-image--glove" style="left:853px;top:253px;width:68px;height:68px;" role="img" aria-label="Grey and red motorcycle glove"></div>
    <span class="price-was" style="left:927px;top:277px;">$49.95</span>
    <span class="price-now" style="left:926px;top:284px;">$47.75</span>
  </section>
</main>
</body>
</html>
```